Business Card Design for videographer/filmmaker - Dale Voss

Looking for a professional, creative, eye catching business card.
Target Market(s)
high end, big budget, businesses, producers, filmmakers, and studios
Industry/Entity Type
Business
Contact Information for Business Card
Please be creative and submit something original.
Font styles to use
Requirements
Must have
- Dale Voss
- creative producer, writer, director, cinematographer, editor
- Pre-production, production, post-production

```html
<!DOCTYPE html>
<html lang="en">
<head>
<meta charset="utf-8">
<title>Dale Voss – Business Card</title>
<link rel="stylesheet" href="https://fonts.googleapis.com/css2?family=Fira+Sans:wght@500;600&display=swap">
<style>
  :root {
    --backdrop: #2b2b2d;
    --card: #f7f7f5;
    --band-light: #d8ccb3;
    --band-dark: #9c8d70;
    --ink: #1c1c1c;
    --name-blue: #1f6688;
    --contact-blue: #2a5f86;
    --muted: #5a5a5a;
    --tree-dark: #2a2a2a;
    --tree-light: #8a8a8a;
    --reel-dark: #5d6878;
    --reel-light: #c9d0da;
    --pin-red: #d8412f;
    --globe-green: #6aa636;
    --mail-blue: #4a7fb7;
  }
  * { margin: 0; padding: 0; box-sizing: border-box; }
  html, body { width: 1200px; height: 800px; overflow: hidden; }
  body {
    background: var(--backdrop);
    font-family: "Fira Sans", Arial, sans-serif;
    position: relative;
  }
  .card {
    position: absolute;
    left: 180px; top: 160px;
    width: 840px; height: 480px;
    background: var(--card);
    overflow: hidden;
  }
  .card__band {
    position: absolute; left: 0; right: 0; height: 20px;
    background: linear-gradient(90deg, var(--band-dark), var(--band-light) 50%, var(--band-dark));
  }
  .card__band--top { top: 0; }
  .card__band--bottom { bottom: 0; }
  .tree-illustration {
    position: absolute; left: 95px; top: 40px;
    width: 250px; height: 190px;
    border-radius: 50% 50% 12% 12%;
    background: radial-gradient(ellipse at 50% 40%, var(--tree-dark), var(--tree-light) 75%, transparent 76%);
    opacity: 0.85;
  }
  .studio-name {
    position: absolute; left: 60px; top: 240px; width: 320px;
    text-align: center;
    font-size: 38px; font-weight: 600; color: var(--ink); letter-spacing: 1px;
    line-height: 48px;
  }
  .person-name {
    position: absolute; left: 60px; top: 298px; width: 320px;
    text-align: center;
    font-size: 44px; font-weight: 600; color: var(--name-blue); line-height: 54px;
  }
  .contact {
    position: absolute; left: 490px; top: 40px;
    list-style: none;
    color: var(--contact-blue); font-weight: 600; font-size: 22px; line-height: 28px;
  }
  .contact__item { display: flex; align-items: flex-start; gap: 12px; margin-bottom: 14px; }
  .contact__item svg { flex: none; margin-top: 4px; }
  .contact__item--tight { margin-bottom: 4px; }
  .film-illustration {
    position: absolute; left: 480px; top: 262px;
    width: 310px; height: 112px;
    border-radius: 36px;
    background: linear-gradient(135deg, var(--reel-light), var(--reel-dark) 55%, var(--reel-light));
    opacity: 0.8;
  }
  .credits {
    position: absolute; left: 0; right: 0; top: 392px;
    text-align: center; color: var(--muted);
    font-size: 16px; font-weight: 500; line-height: 24px;
  }
  .credits__services { color: var(--contact-blue); font-weight: 600; }
</style>
</head>
<body>
  <main class="card">
    <div class="card__band card__band--top"></div>

    <div class="tree-illustration" role="img" aria-label="Ink illustration of a bare, wide-branched tree"></div>

    <p class="studio-name">VOSS STUDIOS</p>
    <p class="person-name">Dale Voss</p>

    <ul class="contact">
      <li class="contact__item">
        <svg width="18" height="22" viewBox="0 0 18 22"><rect x="2" y="1" width="14" height="20" rx="2" fill="none" stroke="#666" stroke-width="2"/><rect x="5" y="4" width="8" height="11" fill="#999"/></svg>
        <span>903-555-0148</span>
      </li>
      <li class="contact__item">
        <svg width="18" height="24" viewBox="0 0 18 24"><path d="M9 1a7 7 0 0 1 7 7c0 6-7 15-7 15S2 14 2 8a7 7 0 0 1 7-7z" fill="var(--pin-red)"/><circle cx="9" cy="8" r="2.5" fill="#fff"/></svg>
        <span>1480 Alder Lane<br>Bay Area<br>CA-94012</span>
      </li>
      <li class="contact__item contact__item--tight">
        <svg width="22" height="16" viewBox="0 0 22 16"><rect x="1" y="1" width="20" height="14" fill="#dfe9f5" stroke="var(--mail-blue)" stroke-width="1.5"/><path d="M1 1l10 8 10-8" fill="none" stroke="var(--mail-blue)" stroke-width="1.5"/></svg>
        <span>info@vossstudios.com</span>
      </li>
      <li class="contact__item">
        <svg width="20" height="20" viewBox="0 0 20 20"><circle cx="10" cy="10" r="8" fill="var(--globe-green)"/><path d="M2 10h16M10 2c4 4 4 12 0 16M10 2c-4 4-4 12 0 16" fill="none" stroke="#fff" stroke-width="1"/></svg>
        <span>www.vossstudios.com</span>
      </li>
    </ul>

    <div class="film-illustration" role="img" aria-label="Illustration of a curling strip of film reel"></div>

    <div class="credits">
      <p class="credits__roles">Creative Producer · Writer · Director · Cinematographer · Editor</p>
      <p class="credits__services">Pre-production · Production · Post-production</p>
    </div>

    <div class="card__band card__band--bottom"></div>
  </main>
</body>
</html>
```